Product Line Brochure

Would like to have a bifold brochure for our product line to show to customers. Would like it to incorporate the paragraph description of the product line with the picture, followed by the product listings. I would like the brochure to be clean and modern. We are a specialty chemical manufacturer in NJ area.

```html
<!DOCTYPE html>
<html lang="en">
<head>
<meta charset="utf-8">
<title>Meridian Coatings – Product Line Brochure</title>
<link rel="stylesheet" href="https://fonts.googleapis.com/css2?family=Montserrat:wght@400;500;600;700;800&family=Open+Sans:wght@400;600&display=swap">
<style>
:root{
  --red:#c8202d;
  --red-light:#d9474f;
  --red-dark:#5c0008;
  --ink:#1a1a1a;
  --text:#444;
  --grey:#c9cacc;
  --grey-dark:#3e3f42;
  --paper:#ffffff;
  --stage:#e4e5e7;
  --head:'Montserrat',sans-serif;
  --body:'Open Sans',sans-serif;
}
*{box-sizing:border-box;margin:0;padding:0}
html,body{width:1200px;height:1200px;overflow:hidden}
body{background:var(--stage);font-family:var(--body);color:var(--text);position:relative}
.spread{position:absolute;left:40px;width:1120px;height:540px;display:flex;box-shadow:0 4px 18px rgba(0,0,0,.18)}
.spread--outer{top:40px}
.spread--inner{top:620px}
.page{position:relative;width:560px;height:540px;background:var(--paper);overflow:hidden}

/* cover */
.cover{background:linear-gradient(135deg,var(--red-light) 0%,#a8141e 45%,var(--red-dark) 100%);color:#fff}
.cover__title{position:absolute;left:50px;top:70px;font-family:var(--head);font-weight:800;font-size:52px;line-height:1.05;letter-spacing:1px}
.cover__contact{position:absolute;left:50px;bottom:50px;font-size:14px;line-height:1.55}
.cover__contact ul{list-style:none;margin-top:6px}
.cover__contact li{display:flex;align-items:center;gap:10px}
.cover__contact svg{width:14px;height:14px;fill:#fff}

/* presence */
.presence__title{position:absolute;right:40px;top:36px;text-align:right;font-family:var(--head)}
.presence__title h2{color:var(--red);font-size:24px;font-weight:700;letter-spacing:.5px}
.presence__title p{color:var(--ink);font-size:14px;font-weight:700;margin-top:2px;margin-right:60px}
.presence__shapes{position:absolute;left:0;top:0}
.presence__photo{position:absolute;left:290px;top:120px;width:270px;height:210px;background:linear-gradient(180deg,#8996ad 0%,#b9bcc0 45%,#6d6a66 100%)}
.presence__caption{position:absolute;left:290px;top:330px;width:270px;height:56px;background:var(--grey);padding:10px 16px;font-size:11px;line-height:1.45;color:#333}
.presence__offices{position:absolute;left:40px;top:440px;display:grid;grid-template-columns:auto auto;gap:6px 30px;font-size:11px;color:#555}
.presence__offices span{display:flex;align-items:center;gap:6px}
.pin{width:9px;height:11px;fill:var(--red)}

/* inner left */
.section-head{font-family:var(--head);font-weight:700;color:var(--red);position:relative;padding-top:10px;line-height:1.2}
.section-head::before{content:"";position:absolute;left:0;top:0;width:50px;height:2px;background:var(--ink)}
.about{position:absolute;left:40px;top:34px;width:480px}
.about .section-head{font-size:25px}
.about p{font-size:11.5px;line-height:1.5;margin-top:6px}
.about__label{color:var(--red);font-size:11.5px;margin-top:4px}
.about ul{list-style:none;font-size:11.5px;line-height:1.45;margin-top:2px}
.about li::before{content:"★";color:var(--red);font-size:9px;margin-right:8px}
.arch{position:absolute;left:40px;top:244px;width:480px}
.arch .section-head{font-size:21px;white-space:nowrap}
.arch h4{font-family:var(--head);font-weight:500;font-size:11.5px;color:#666;margin-top:3px;letter-spacing:.5px}
.arch p{font-size:11px;line-height:1.45;margin-top:5px;width:250px}
.photo-drop{position:absolute;right:30px;top:292px;width:210px;height:104px;border-radius:12px;background:radial-gradient(circle at 45% 45%,#c9c7c4 0%,#7a6a5c 35%,#3d3530 100%)}
.photo-plant{position:absolute;left:40px;top:416px;width:490px;height:96px;background:linear-gradient(180deg,#1e2633 0%,#3f4a5a 55%,#2a3f3a 100%)}
.band{position:absolute;left:0;right:0;bottom:0;height:14px;background:var(--red)}

/* inner right */
.products{padding:30px 28px}
.products h3{font-family:var(--head);font-weight:700;color:var(--red);font-size:18px;margin-bottom:6px}
.ptable{width:100%;border-collapse:collapse;font-size:9.5px;margin-bottom:22px}
.ptable th{background:var(--ink);color:#fff;font-weight:600;font-family:var(--head);font-size:9.5px;text-align:left;padding:4px 6px;border-right:3px solid #fff}
.ptable th.tag{background:var(--red)}
.ptable td{padding:6px 6px;border-bottom:1px solid #e6e6e6;vertical-align:top;line-height:1.3}
.ptable td.name{font-family:var(--head);font-weight:600;color:#333;white-space:nowrap}
.ptable td.desc{font-size:8px;color:#666;width:34%}
</style>
</head>
<body>

<section class="spread spread--outer">
  <article class="page cover">
    <h1 class="cover__title">MERIDIAN<br>COATINGS, INC.</h1>
    <div class="cover__contact">
      <p>MCI Headquarters R&amp;D/Manufacturing/Sales<br>215 Riverside Ave, Lyndhurst, NJ 07071</p>
      <ul>
        <li><svg viewBox="0 0 16 16"><path d="M3 1l3 3-2 2c1 2 3 4 5 5l2-2 3 3-2 3C6 15 1 10 0 3z"/></svg>000 - 000 - 0000</li>
        <li><svg viewBox="0 0 16 16"><path d="M0 3h16v10H0zM1 4l7 5 7-5v-.2H1z" fill-rule="evenodd"/></svg>info.companyname.com</li>
        <li><svg viewBox="0 0 16 16"><circle cx="8" cy="8" r="7.5"/></svg>www.companyname.com</li>
      </ul>
    </div>
  </article>

  <article class="page presence">
    <svg class="presence__shapes" width="560" height="540" viewBox="0 0 560 540" aria-hidden="true">
      <path d="M0 110 Q140 140 270 120 V330 L0 330 Z" fill="var(--grey-dark)"/>
      <path d="M0 80 Q140 120 270 105 L270 110 Q140 135 0 110 Z" fill="#fff"/>
      <path d="M200 110 H270 V410 L140 330 H200 Z" fill="var(--red)"/>
      <path d="M270 100 L290 115 L270 115 Z" fill="var(--red)"/>
    </svg>
    <div class="presence__title">
      <h2>MERIDIAN COATINGS, INC.</h2>
      <p>OUR PRESENCE</p>
    </div>
    <div class="presence__photo" role="img" aria-label="Photo of the headquarters manufacturing plant with steel structures and a crane"></div>
    <div class="presence__caption">MCI Headquarters R&amp;D/Manufacturing/Sales<br>215 Riverside Ave, Lyndhurst, NJ 07071</div>
    <div class="presence__offices">
      <span><svg class="pin" viewBox="0 0 10 12"><path d="M5 0a4 4 0 014 4c0 3-4 8-4 8S1 7 1 4a4 4 0 014-4z"/></svg>IL - Technical Sales</span>
      <span><svg class="pin" viewBox="0 0 10 12"><path d="M5 0a4 4 0 014 4c0 3-4 8-4 8S1 7 1 4a4 4 0 014-4z"/></svg>NC - Technical Sales</span>
      <span><svg class="pin" viewBox="0 0 10 12"><path d="M5 0a4 4 0 014 4c0 3-4 8-4 8S1 7 1 4a4 4 0 014-4z"/></svg>MI - Technical Sales</span>
      <span><svg class="pin" viewBox="0 0 10 12"><path d="M5 0a4 4 0 014 4c0 3-4 8-4 8S1 7 1 4a4 4 0 014-4z"/></svg>GA - Technical Sales</span>
    </div>
  </article>
</section>

<section class="spread spread--inner">
  <article class="page applications">
    <div class="about">
      <h2 class="section-head">About Us</h2>
      <p>Innovative specialty chemicals for almost 40 years. We combine a wealth of experience, with R&amp;D resources and the responsiveness of our technical and customer service team to support our customers.</p>
      <p class="about__label">Industries including:</p>
      <ul>
        <li>Architectural</li>
        <li>Textiles &amp; Leather</li>
        <li>Inks, Paints &amp; Coatings</li>
        <li>Adhesives/Adhesion Promoters</li>
      </ul>
    </div>
    <div class="arch">
      <h2 class="section-head">Architectural Applications</h2>
      <h4>WATER, OIL AND STAIN REPELLENTS</h4>
      <p>Meridian Coatings, Inc. offers a variety of materials used to impart barrier properties to surfaces such as concrete, grout, natural stone, pavers, wood and others. These sealers shield against water, oil, stains as well as corrosion and freeze-thaw damage.</p>
    </div>
    <div class="photo-drop" role="img" aria-label="Close-up photo of a water droplet beading on a treated surface"></div>
    <div class="photo-plant" role="img" aria-label="Night photo of an illuminated chemical plant"></div>
    <div class="band"></div>
  </article>

  <article class="page products">
    <h3>Water, Oil &amp; Stain Repellents - Waterborne</h3>
    <table class="ptable">
      <thead><tr><th class="tag">Product</th><th>Actives (%)</th><th>pH</th><th>Ionic character</th><th>Description</th></tr></thead>
      <tbody>
        <tr><td class="name">MCI-BR795</td><td>20.0</td><td>3.0 – 5.0</td><td>Non-ionic</td><td class="desc">Modified fluorinated product, stable at room temperature, cures with heat.</td></tr>
        <tr><td class="name">MCI-NS101</td><td>25.0</td><td>3.0 – 5.0</td><td>Cationic</td><td class="desc">Silicone and fluorine free water repellent finish for fabrics.</td></tr>
        <tr><td class="name">DuraShield® 732</td><td>19.0</td><td>3.0 – 5.0</td><td>Cationic</td><td class="desc">Short chain fluoropolymer with exceptional soil release properties.</td></tr>
        <tr><td class="name">DuraShield® 775</td><td>20.0</td><td>3.0 – 5.0</td><td>Cationic</td><td class="desc">Short chain fluoropolymer giving water and oil repellency to all fabrics.</td></tr>
        <tr><td class="name">DuraShield® 734</td><td>30.0</td><td>3.0 – 5.0</td><td>Cationic</td><td class="desc">Short chain fluoropolymer that imparts water, oil and soil repellency to textiles.</td></tr>
      </tbody>
    </table>
    <h3>Fabric &amp; Leather Protectants- Solventborne</h3>
    <table class="ptable">
      <thead><tr><th class="tag">Product</th><th>Actives (%)</th><th>Carrier</th><th>VOCs (g/L)</th><th>Description</th></tr></thead>
      <tbody>
        <tr><td class="name">MCS-232HC</td><td>50.0</td><td>Octamethylcyclo­tetrasiloxane</td><td></td><td class="desc">Silicone based super-hydrophobic treatment for fabrics and leather.</td></tr>
        <tr><td class="name">DuraShield® 805</td><td>18.5</td><td>n-butyl acetate<br>odorless mineral spirits</td><td>700</td><td class="desc">Short chain fluoropolymer water, oil and stain repellent for fabrics.</td></tr>
        <tr><td class="name">DuraShield® 816</td><td>18.5</td><td>n-butyl acetate<br>ethyl acetate<br>odorless mineral spirits</td><td></td><td class="desc">Short chain fluoropolymer with exceptional repellency for aftermarket use.</td></tr>
      </tbody>
    </table>
    <div class="band"></div>
  </article>
</section>

</body>
</html>
```